2015 Conference Header

I would like a header designed for our conference next year. It will be used on all of our event promotional material. The information and images that can be used are in the drop box file. I have also included examples of what we have used in the past.

https://www.filevaultly.example/sh/7k2p4x9q1m3nz8/QWErty834LmnoPzx5TuvBn2Ck?dl=0

Industry/Entity Type

Event

Requirements
Must have
• To give you all a little more idea on our branding colours and designs our business website is www.harbecklanefab.example

```html
<!DOCTYPE html>
<html lang="en">
<head>
<meta charset="utf-8">
<title>Polyspin 2015 Letterhead</title>
<link rel="stylesheet" href="https://fonts.googleapis.com/css2?family=Roboto+Slab:wght@300;400&display=block">
<style>
  :root {
    --page: #ffffff;
    --band: rgba(24, 24, 24, 0.95);
    --text-light: #ffffff;
    --sky-top: #e9a46a;
    --sky-mid: #c98a6a;
    --sea: #7a5b5e;
    --sea-deep: #3d2c30;
    --sand: #a07a6a;
  }
  * { margin: 0; padding: 0; box-sizing: border-box; }
  html, body {
    width: 962px;
    height: 1200px;
    overflow: hidden;
    background: var(--page);
  }
  .letterhead {
    position: relative;
    width: 962px;
    height: 1200px;
    background: var(--page);
  }
  .header {
    position: relative;
    width: 100%;
    height: 305px;
  }
  .header-photo {
    position: absolute;
    inset: 0;
    background: linear-gradient(
      to bottom,
      var(--sky-top) 0%,
      var(--sky-top) 30%,
      var(--sky-mid) 36%,
      var(--sea) 52%,
      var(--sea-deep) 78%,
      var(--sand) 100%
    );
  }
  .title-band {
    position: absolute;
    top: 0;
    left: 0;
    width: 100%;
    height: 88px;
    background: var(--band);
    color: var(--text-light);
    font-family: "Roboto Slab", "Rockwell", "Courier New", serif;
  }
  .event-name {
    position: absolute;
    left: 13px;
    top: 6px;
    font-size: 45px;
    font-weight: 400;
    line-height: 1.1;
    white-space: nowrap;
  }
  .event-location {
    position: absolute;
    right: 596px;
    top: 58px;
    text-align: right;
    font-size: 21px;
    font-weight: 400;
    line-height: 1.1;
    white-space: nowrap;
  }
  .event-dates {
    position: absolute;
    right: 18px;
    top: 12px;
    font-size: 27px;
    font-weight: 400;
    line-height: 1.1;
    white-space: nowrap;
  }
  .event-dates sup { font-size: 15px; line-height: 0; }
  .event-url {
    position: absolute;
    right: 16px;
    top: 55px;
    font-size: 21px;
    font-weight: 400;
    line-height: 1.1;
    white-space: nowrap;
  }
</style>
</head>
<body>
  <div class="letterhead">
    <header class="header">
      <div class="header-photo" role="img" aria-label="Sunset beach photo: people walking through the shallows beside a wooden jetty"></div>
      <div class="title-band">
        <h1 class="event-name">Polyspin 2015</h1>
        <p class="event-location">Adelaide, Australia</p>
        <p class="event-dates">21<sup>st</sup>– 23<sup>rd</sup> June</p>
        <p class="event-url">www.mouldersummit.example</p>
      </div>
    </header>
  </div>
</body>
</html>
```